Business card design for a Cloud Service Provider Company

We already have business card and would like to update and get a different design. Our company is Managed IT services and Cloud Solutions Company, Tevro Systems. Attached is our current logo, current business card and sample design. I am not sure if we still need to keep our partners details on the back of the card as it does not look good to me... Please let me know if you need any additional information...

Target Market(s)

Any verticals with IT infrastructure - CEOs, CFOs and CIOs

Industry/Entity Type

Information Technology

Requirements
Must have
• First Name Last Name
• Phone
• Email address
• Company Logo

```html
<!DOCTYPE html>
<html lang="en">
<head>
<meta charset="utf-8">
<title>Tevro Systems – Business Cards</title>
<link rel="stylesheet" href="https://fonts.googleapis.com/css2?family=Arimo:wght@400;700&display=swap">
<style>
  :root {
    --bg: #b9b9b9;
    --card: #ffffff;
    --ink: #111111;
    --muted: #2a2a2a;
    --blue: #1ea7e1;
    --green: #9bd43a;
  }
  * { box-sizing: border-box; margin: 0; padding: 0; }
  html, body { width: 1200px; height: 960px; overflow: hidden; }
  body {
    background: var(--bg);
    font-family: "Arimo", Arial, sans-serif;
    color: var(--ink);
    display: flex;
    flex-direction: column;
    align-items: center;
    justify-content: center;
    gap: 40px;
  }
  .card {
    width: 720px;
    height: 412px;
    background: var(--card);
    position: relative;
    box-shadow: 0 6px 18px rgba(0,0,0,.18);
  }
  .wordmark {
    display: flex;
    align-items: center;
    gap: 14px;
  }
  .wordmark-name {
    font-weight: 700;
    color: var(--ink);
    letter-spacing: -0.02em;
    line-height: 1;
  }
  .wordmark-dot {
    border-radius: 50%;
    background: var(--blue);
  }
  .tagline {
    color: var(--muted);
    font-weight: 400;
    letter-spacing: 0.01em;
  }

  /* Front */
  .card-front .brand {
    position: absolute;
    left: 50%;
    top: 50%;
    transform: translate(-50%, -50%);
    display: flex;
    flex-direction: column;
    align-items: flex-end;
  }
  .card-front .wordmark-name { font-size: 120px; }
  .card-front .wordmark-dot { width: 34px; height: 34px; }
  .card-front .tagline { font-size: 26px; margin-top: 6px; }

  /* Back */
  .card-back .contact {
    position: absolute;
    left: 44px;
    top: 40px;
    font-size: 16px;
    line-height: 1.3;
  }
  .person-name { font-weight: 700; font-size: 19px; }
  .person-role { font-size: 16px; margin-bottom: 22px; }
  .contact-line .label { font-weight: 700; margin-right: 4px; }

  .card-back .brand {
    position: absolute;
    right: 44px;
    top: 118px;
    display: flex;
    flex-direction: column;
    align-items: flex-end;
  }
  .card-back .wordmark-name { font-size: 64px; }
  .card-back .wordmark-dot { width: 18px; height: 18px; }
  .card-back .wordmark { gap: 8px; }
  .card-back .tagline { font-size: 15px; margin-top: 4px; }

  .card-back .office {
    position: absolute;
    right: 44px;
    bottom: 36px;
    text-align: right;
    font-size: 16px;
    line-height: 1.3;
  }
  .office .label { font-weight: 700; margin-right: 4px; }
  .office .web { font-weight: 700; }
</style>
</head>
<body>

  <section class="card card-front" aria-label="Front of business card">
    <div class="brand">
      <div class="wordmark">
        <span class="wordmark-name">tevro</span>
        <span class="wordmark-dot" aria-hidden="true"></span>
      </div>
      <p class="tagline">Cloud Service Provider</p>
    </div>
  </section>

  <section class="card card-back" aria-label="Back of business card">
    <div class="contact">
      <p class="person-name">Reid L. Varnholt</p>
      <p class="person-role">Technical Manager</p>
      <p class="contact-line">reid.varnholt@tevro.com.au</p>
      <p class="contact-line"><span class="label">p</span>+61 (2) 5550 1015</p>
      <p class="contact-line"><span class="label">m</span>+61 (0) 400 555 218</p>
    </div>

    <div class="brand">
      <div class="wordmark">
        <span class="wordmark-name">tevro</span>
        <span class="wordmark-dot" aria-hidden="true"></span>
      </div>
      <p class="tagline">Cloud Service Provider</p>
    </div>

    <address class="office" style="font-style: normal;">
      <p>Suite 204, 12-14 Harlow Street</p>
      <p>Eastwood Park NSW 2071, Australia</p>
      <p><span class="label">Main</span>+61 (2) 5550 0104</p>
      <p><span class="label">Support</span>1300 555 400</p>
      <p class="web">www.tevro.com.au</p>
    </address>
  </section>

</body>
</html>
```